yourSmileCare Brookvale Business Card

Please design a two sided business card that is Elegant and Professional
Add subtle elegant patterns to suit Spot UV printing/ or raised printing

Name: Dr Marcus T. Fenwick
Qualification: BDSc (QLD)
Title: Dental Surgeon, Clinical Director
Company: yourSmileCare Brookvale
Phone: (02) 7593 2268
Address: Shop 7/18-20 Lindon Ave Brookvale 2097
email: info@yoursmilecarebrookvale.com.au
Facebook: facebook.com/yoursmilecarebrookvale

Motto:
Quality dentistry you can trust

Description of services (not compulsory):
Preventative Dentistry | General Dentistry
Cosmetic Dentistry | Teeth Whitening
Crown and Bridge | Root Canal Therapy
Veneers | Clearvono | Orthodontics
Emergency Dental Care | After Hours

Personalised Treatment Plans
Transparent Fees

Please make sure card is elegant and professional

Target Market(s)

general population, patients,
Dental sales companies, other professions

Industry/Entity Type

Dental Clinic

Contact Information for Business Card

Name: Dr Marcus T. Fenwick
Qualification: BDSc (QLD)
Phone: (02) 7593 2268
Address: Shop 7/18-20 Lindon Ave Brookvale

Motto:

Description of services (not compulsory)

Transparent Fees

Image of dental surgery optional

Please make sure card is elegant and profession

Requirements
Must have
• Logo
• Name, Title (next to name), Business
• Phone, address, facbeook
• Must have stylish design to suit SPOT UV reflective printing
Nice to have
• Subtle elegant patterns which will have Spot UV on them when printed
• Colours to match logo colour
• Description of services
Should not have
• Small fonts that are hard to read
• DO NOT PUT IMAGES OF DENTAL INSTRUMENTS OR TEETH PLEASE

```html
<!DOCTYPE html>
<html lang="en">
<head>
<meta charset="utf-8">
<title>yourSmileCare Brookvale – Business Card</title>
<link href="https://fonts.googleapis.com/css2?family=Roboto:wght@400;500;700&display=swap" rel="stylesheet">
<style>
  :root {
    --green: #8fc043;
    --green-dark: #7fb036;
    --grey: #77777a;
    --grey-light: #c9c9cb;
    --ink: #4a4a4c;
    --paper: #ffffff;
    --backdrop: #d5d5d7;
  }
  * { box-sizing: border-box; margin: 0; padding: 0; }
  html, body { width: 1200px; height: 990px; overflow: hidden; }
  body {
    background: var(--backdrop);
    font-family: "Roboto", Arial, sans-serif;
    display: flex;
    align-items: center;
    justify-content: center;
    gap: 48px;
  }
  .card {
    position: relative;
    width: 540px;
    height: 300px;
    border-radius: 14px;
    overflow: hidden;
    box-shadow: 0 4px 10px rgba(0,0,0,.22);
  }
  /* front */
  .card--front { background: var(--paper); }
  .card__waves { position: absolute; inset: 0; width: 100%; height: 100%; }
  .holder { position: absolute; left: 32px; top: 52px; }
  .holder__name { color: var(--green-dark); font-weight: 700; font-size: 18px; letter-spacing: .2px; }
  .holder__title { color: var(--ink); font-size: 12px; margin-top: 3px; }
  .holder__title .sep { color: var(--green); }
  .holder__qual { color: var(--green); font-size: 12px; margin-top: 1px; }
  .brand {
    position: absolute; right: 36px; top: 58px; text-align: right;
    font-weight: 500; color: var(--grey);
  }
  .brand__mark { display: inline-block; width: 14px; height: 14px; border-radius: 50%; background: var(--green); vertical-align: middle; margin-right: 6px; }
  .brand__name { font-size: 25px; line-height: 1.05; vertical-align: middle; }
  .brand__place { display: block; font-size: 18px; letter-spacing: 1px; }
  .contact { position: absolute; left: 34px; bottom: 28px; list-style: none; color: #fff; font-size: 12px; }
  .contact li { display: flex; align-items: center; gap: 7px; line-height: 18px; }
  .contact svg { width: 12px; height: 12px; flex: none; }
  .address { position: absolute; right: 36px; bottom: 30px; color: #fff; font-size: 12px; text-align: right; line-height: 16px; }
  /* back */
  .card--back { background: var(--green); display: flex; flex-direction: column; align-items: center; justify-content: center; color: #fff; }
  .card__pattern { position: absolute; inset: 0; background: linear-gradient(135deg, #93c447, #88ba3c); }
  .back__brand { position: relative; text-align: center; font-weight: 500; }
  .back__brand .brand__mark { background: #fff; }
  .back__brand .brand__name { font-size: 36px; }
  .back__brand .brand__place { font-size: 24px; letter-spacing: 1.5px; }
  .back__web { position: relative; font-size: 13px; margin-top: 26px; }
</style>
</head>
<body>

<section class="card card--front" aria-label="Business card front">
  <svg class="card__waves" viewBox="0 0 540 300" preserveAspectRatio="none" aria-hidden="true">
    <path d="M0 148 C120 120 230 130 330 158 C420 184 480 184 540 172 L540 186 C480 200 420 200 330 176 C230 148 120 142 0 164 Z" fill="var(--grey)"/>
    <path d="M0 164 C120 142 230 148 330 176 C420 200 480 200 540 186 L540 206 C480 214 420 212 330 190 C230 162 120 158 0 178 Z" fill="var(--grey-light)"/>
    <path d="M0 172 C120 154 230 160 330 186 C420 210 480 212 540 202 L540 300 L0 300 Z" fill="var(--green)"/>
  </svg>

  <div class="holder">
    <p class="holder__name">DR MARCUS T. FENWICK</p>
    <p class="holder__title">Dental Surgeon <span class="sep">/</span> Clinical Director</p>
    <p class="holder__qual">BDSc (QLD)</p>
  </div>

  <div class="brand">
    <span class="brand__mark"></span><span class="brand__name">yourSmileCare</span>
    <span class="brand__place">BROOKVALE</span>
  </div>

  <ul class="contact">
    <li><svg viewBox="0 0 12 12"><rect width="12" height="12" rx="2" fill="#fff"/><path d="M3.5 2.5l1.5 0 .6 2-1 .8c.5 1 1.2 1.7 2.1 2.1l.8-1 2 .6v1.5c-3.5.2-6.2-2.5-6-6z" fill="var(--green)"/></svg>(02) 7593 2268</li>
    <li><svg viewBox="0 0 12 12"><rect width="12" height="12" rx="2" fill="#fff"/></svg>facebook.com/yoursmilecarebrookvale</li>
    <li><svg viewBox="0 0 12 12"><rect width="12" height="12" rx="2" fill="#fff"/><path d="M2.5 3.5h7v5h-7z M2.5 3.5l3.5 2.7 3.5-2.7" fill="none" stroke="var(--green)" stroke-width="1"/></svg>info@yoursmilecarebrookvale.com.au</li>
  </ul>

  <p class="address">Shop 7/18-20 Lindon Ave<br>Brookvale 2097</p>
</section>

<section class="card card--back" aria-label="Business card back">
  <div class="card__pattern" role="img" aria-label="Subtle tonal repeat pattern for spot UV finish"></div>
  <div class="back__brand">
    <span class="brand__mark"></span><span class="brand__name">yourSmileCare</span>
    <span class="brand__place">BROOKVALE</span>
  </div>
  <p class="back__web">www.yoursmilecarebrookvale.com.au</p>
</section>

</body>
</html>
```